Want to incorporate elements of all these items to make an amazing sign to welcome people to the community. The sign is 6x4 and needs to incorporate the following items:

Welcome to Corwick Meadows

Come visit the PRD sales center at 745 thistledown road
High Speed Fiber Internet
Land financing starting at $299 (No credit checks)
Let us build your dream home!
555-284-7390
We like the gold and black design no teal or blue that was another agents design. Some combination of the current sign all the stuff listed above and then design elements that tie into the truck wrap.

Target Market(s)

People visiting the neighborhood

Industry/Entity Type

real estate and construction

Font styles to use
Serif

Colors

Designer to choose colors to be used in the design.

Requirements
Must have
• PRD Home Builders Welcomes you to Corwick Meadows, Let us build your dream home, Phone number, Land financing starting at $299 NO credit checks

```html
<!DOCTYPE html>
<html lang="en">
<head>
<meta charset="UTF-8">
<title>Corwick Meadows Welcome Sign</title>
<link href="https://fonts.googleapis.com/css2?family=Outfit:wght@400;500;600;700&family=Nothing+You+Could+Do&display=swap" rel="stylesheet">
<style>
  :root {
    --gold: #937a4a;
    --gold-light: #b59a63;
    --ink: #151212;
    --paper: #ffffff;
    --stage: #e9e8e6;
    --frame: #d4d4d2;
    --muted: #8a8a8a;
  }
  * { margin: 0; padding: 0; box-sizing: border-box; }
  html, body {
    width: 1200px; height: 900px; overflow: hidden;
    background: var(--stage);
    font-family: "Outfit", sans-serif;
  }
  .sign {
    position: absolute; left: 40px; top: 75px;
    width: 1120px; height: 750px;
    background: var(--paper);
    border: 6px solid var(--frame);
  }
  .sign > * { position: absolute; }
  .welcome {
    left: 52px; top: 44px;
    font-size: 66px; font-weight: 500; color: var(--gold);
    letter-spacing: 0.5px; white-space: nowrap;
  }
  .phone {
    left: 44px; top: 118px;
    font-size: 158px; font-weight: 600; color: var(--ink);
    letter-spacing: -2px; line-height: 1; white-space: nowrap;
  }
  .home-render {
    left: 250px; top: 270px; width: 790px; height: 420px;
    background:
      radial-gradient(ellipse at 50% 45%, #8a6448 0%, #6e5646 30%, rgba(120,110,95,0.5) 55%, rgba(255,255,255,0) 72%),
      radial-gradient(ellipse at 88% 30%, rgba(160,140,70,0.55) 0%, rgba(255,255,255,0) 30%),
      radial-gradient(ellipse at 8% 40%, rgba(160,140,70,0.45) 0%, rgba(255,255,255,0) 28%);
  }
  .tag {
    height: 28px; padding: 0 22px;
    background: var(--ink); color: var(--paper);
    font-size: 15px; font-weight: 500;
    display: flex; align-items: center; white-space: nowrap;
    clip-path: polygon(4% 0, 100% 0, 96% 100%, 0 100%);
  }
  .tag-financing { left: 58px; top: 318px; }
  .tag-fiber { left: 122px; top: 446px; }
  .price {
    left: 82px; top: 348px; width: 280px; height: 68px;
    background: var(--gold);
    clip-path: polygon(0 0, 92% 0, 100% 55%, 94% 100%, 7% 100%);
    color: var(--paper); font-size: 48px; font-weight: 500;
    display: flex; align-items: center; justify-content: center;
    padding-right: 30px;
  }
  .tagline {
    left: 420px; top: 455px; width: 460px;
    font-family: "Nothing You Could Do", cursive;
    font-size: 44px; line-height: 1.1; color: var(--paper);
    transform: rotate(-12deg);
    text-align: center;
  }
  .brand {
    left: 48px; top: 578px;
    font-size: 104px; font-weight: 600; color: var(--gold);
    line-height: 1; letter-spacing: -2px;
  }
  .visit {
    left: 52px; top: 694px;
    font-size: 14px; font-weight: 500; color: var(--ink);
    white-space: nowrap;
  }
  .fine-print {
    right: 56px; top: 680px;
    font-size: 11px; color: var(--muted);
  }
</style>
</head>
<body>
  <main class="sign">
    <h1 class="welcome">Welcome to Corwick Meadows</h1>
    <p class="phone">555-284-7390</p>
    <div class="home-render" role="img" aria-label="Rendering of a modern two-storey wood and glass home with landscaping and trees"></div>
    <p class="tag tag-financing">Land financing starting at</p>
    <p class="price">$299</p>
    <p class="tag tag-fiber">High Speed Fiber Internet</p>
    <p class="tagline">Let us build your dream home!</p>
    <p class="brand">PRD</p>
    <p class="visit">Come visit the PRD sales center at : 745 Thistledown Rd</p>
    <p class="fine-print">*No credit checks</p>
  </main>
</body>
</html>
```